Amber Hill House Brochure Design

We need a brochure designed for our Aged Care Facility. We need designs that portray warmth and welcoming and at the same time something professional. We have attached the previous brochure and are looking for a modern professional brochure. We are not set on sizing and welcome ideas.

Attachments:
- There are three files attached in this brief.
- One more high res photo is available via this link: https://www.filecrate.example/s/qm42tx7wpe0kdn3/House_High-Res_18.jpg?dl=0
- Another high res file has been added and is available through this link:
https://www.filecrate.example/s/vr83nc1yuf6jlo9/House_High-Res_24.jpg?dl=0

Target Market(s)

Aged Care and families

Requirements
Must have
• Logo and contact details

```html
<!DOCTYPE html>
<html lang="en">
<head>
<meta charset="utf-8">
<title>Amber Hill House Brochure</title>
<link href="https://fonts.googleapis.com/css2?family=Oswald:wght@400;500&family=Open+Sans:ital,wght@0,400;1,400;1,700&display=swap" rel="stylesheet">
<style>
  :root {
    --stage: #e4e4e4;
    --navy: #0a3e5f;
    --sky: #5fb4ee;
    --brand-blue: #2b80cf;
    --paper: #f1f2f3;
    --ink: #1b1b1b;
    --ink-soft: #4a4a4a;
    --heading: #0b3f60;
    --grey-text: #5e6468;
    --white: #ffffff;
  }
  html, body { margin: 0; padding: 0; }
  body {
    width: 1200px; height: 1024px; overflow: hidden;
    background: var(--stage);
    display: flex; align-items: center; justify-content: center;
  }
  .brochure { display: block; width: 1160px; height: 819px; }
  .house-name { font-family: "Open Sans", sans-serif; font-weight: 400; }
  .caps-spaced { font-family: "Open Sans", sans-serif; letter-spacing: 5px; }
  .small-caps-line { font-family: "Open Sans", sans-serif; }
  .heading { font-family: "Oswald", sans-serif; font-weight: 500; }
  .subheading { font-family: "Oswald", sans-serif; font-weight: 400; }
  .contact { font-family: "Open Sans", sans-serif; }
  .intro { font-family: "Open Sans", sans-serif; font-style: italic; }
  .quote { font-family: "Open Sans", sans-serif; font-style: italic; }
  .quote-name { font-family: "Open Sans", sans-serif; font-style: italic; font-weight: 700; }
</style>
</head>
<body>
<svg class="brochure" viewBox="0 0 1382 976" xmlns="http://www.w3.org/2000/svg">
  <defs>
    <linearGradient id="paperGrad" x1="0" y1="0" x2="1" y2="0">
      <stop offset="0" stop-color="#e6e7e8"/>
      <stop offset="0.5" stop-color="#f7f7f7"/>
      <stop offset="1" stop-color="#d6d8da"/>
    </linearGradient>
    <linearGradient id="residentGrad" x1="0" y1="0" x2="1" y2="1">
      <stop offset="0" stop-color="#c9a77c"/>
      <stop offset="0.45" stop-color="#c7d3b8"/>
      <stop offset="1" stop-color="#e8e6e2"/>
    </linearGradient>
    <linearGradient id="roomGrad" x1="0" y1="0" x2="0" y2="1">
      <stop offset="0" stop-color="#e2ddce"/>
      <stop offset="0.55" stop-color="#a89a88"/>
      <stop offset="1" stop-color="#6d6a78"/>
    </linearGradient>
    <linearGradient id="gardenGrad" x1="0" y1="0" x2="0" y2="1">
      <stop offset="0" stop-color="#5a9fd4"/>
      <stop offset="0.4" stop-color="#7f9a6e"/>
      <stop offset="1" stop-color="#a9a9a7"/>
    </linearGradient>
    <linearGradient id="bandGrad" x1="0" y1="0" x2="1" y2="0">
      <stop offset="0" stop-color="#1e6fbd"/>
      <stop offset="1" stop-color="#3a90da"/>
    </linearGradient>
  </defs>

  <rect class="paper" width="1382" height="976" fill="url(#paperGrad)"/>

  <path role="img" aria-label="Photo of a smiling resident seated in the bright lounge"
        d="M0 0 H534 V392 Q534 434 492 434 H0 Z" fill="url(#residentGrad)"/>

  <rect role="img" aria-label="Photo of a furnished resident bedroom" x="548" y="0" width="326" height="275" fill="url(#roomGrad)"/>

  <!-- cover panel -->
  <path d="M900 0 H1382 V235 Q1382 295 1322 295 H900 Z" fill="var(--sky)"/>
  <path d="M889 0 H1352 V212 Q1352 275 1289 275 H889 Z" fill="var(--navy)"/>
  <g class="cover-name" text-anchor="middle">
    <text class="house-name" x="1130" y="160" font-size="28" fill="var(--white)">Amber Hill House</text>
    <text class="caps-spaced" x="1138" y="225" font-size="16" fill="var(--white)">AT AMBER HILL HOUSE,</text>
    <text class="small-caps-line" x="1138" y="245" font-size="11.5" fill="#dbe6ee">WE'RE COMMITTED TO YOUR CARE AND COMFORT</text>
  </g>

  <path d="M0 453 H405 Q448 453 450 410 V345 Q452 295 502 295 H921"
        fill="none" stroke="var(--sky)" stroke-width="6"/>

  <rect role="img" aria-label="Photo of the paved courtyard garden with pergola and benches" x="921" y="295" width="461" height="478" fill="url(#gardenGrad)"/>
  <rect x="921" y="773" width="461" height="109" fill="url(#bandGrad)"/>
  <rect x="921" y="882" width="461" height="7" fill="var(--sky)"/>
  <g text-anchor="middle">
    <text class="heading" x="1151" y="826" font-size="25" fill="var(--white)">PROVIDING AGED CARE WITH QUALITY,</text>
    <text class="heading" x="1151" y="857" font-size="25" fill="var(--white)">DIGNITY AND INDIVIDUALITY</text>
  </g>

  <path d="M0 776 H398 Q442 776 448 820 L452 850 Q458 895 505 895 H1382 V976 H0 Z" fill="var(--navy)"/>
  <path d="M0 766 H400 Q452 766 458 818 L462 848 Q467 885 508 885 H921"
        fill="none" stroke="var(--brand-blue)" stroke-width="6"/>
  <text class="caps-spaced" x="1151" y="943" font-size="14" fill="var(--white)" text-anchor="middle" letter-spacing="3">www.amberhillhouse.example</text>

  <!-- intro -->
  <g text-anchor="middle">
    <text class="intro" x="225" y="543" font-size="23" fill="var(--ink-soft)"><tspan font-weight="700">Amber Hill House</tspan> is an accredited</text>
    <text class="intro" x="225" y="572" font-size="23" fill="var(--ink-soft)">Government funded place...</text>
    <text class="intro" x="222" y="644" font-size="19.5" fill="var(--ink-soft)">...aged care facility offering quality dignity</text>
    <text class="intro" x="222" y="673" font-size="19.5" fill="var(--ink-soft)">and individuality for residents and their</text>
    <text class="intro" x="222" y="702" font-size="19.5" fill="var(--ink-soft)">loved ones.</text>
  </g>

  <!-- testimonial -->
  <g text-anchor="middle">
    <text x="210" y="830" font-family="Georgia, serif" font-size="64" font-weight="700" fill="var(--brand-blue)">“</text>
    <text class="quote" x="210" y="849" font-size="14.5" fill="var(--white)">Overall our mother is happier, she initiates conversa-</text>
    <text class="quote" x="210" y="872" font-size="14.5" fill="var(--white)">tion, her memory has improved. She laughs a lot &amp; still</text>
    <text class="quote" x="210" y="895" font-size="14.5" fill="var(--white)">beats some of us at maths. Her “spark” seems to have</text>
    <text class="quote" x="210" y="918" font-size="14.5" fill="var(--white)">returned. That makes the whole family happy.</text>
    <text class="quote-name" x="210" y="953" font-size="17" fill="var(--white)">Nora Whitfield</text>
  </g>

  <!-- contact panel -->
  <g class="contact-panel" text-anchor="middle">
    <text class="house-name" x="691" y="490" font-size="30" fill="var(--heading)">Amber Hill House</text>
    <text class="heading" x="691" y="559" font-size="31" fill="var(--heading)">CONTACT US TODAY</text>
    <text class="subheading" x="691" y="590" font-size="23" fill="var(--grey-text)">FOR MORE INFORMATION</text>

    <circle cx="685" cy="622" r="10" fill="none" stroke="var(--heading)" stroke-width="1.6"/>
    <path d="M681 617 q-1 6 7 10 l2 -2 -3 -2 -1 1 q-3 -2 -3 -4 l1 -1 -2 -3 z" fill="var(--heading)"/>
    <text class="contact" x="690" y="660" font-size="19" fill="var(--ink)">07 3391 5820</text>

    <circle cx="685" cy="695" r="10" fill="none" stroke="var(--heading)" stroke-width="1.6"/>
    <path d="M685 701 q-5 -6 -5 -9 a5 5 0 0 1 10 0 q0 3 -5 9 z" fill="var(--heading)"/>
    <circle cx="685" cy="692" r="1.8" fill="var(--paper)"/>
    <text class="contact" x="688" y="728" font-size="19" fill="var(--ink)">48 Marlowe Crescent</text>
    <text class="contact" x="688" y="752" font-size="19" fill="var(--ink)">(off Amber Hill Drive)</text>
    <text class="contact" x="688" y="776" font-size="19" fill="var(--ink)">Kellin Vale QLD 4127</text>

    <circle cx="685" cy="807" r="10" fill="none" stroke="var(--heading)" stroke-width="1.6"/>
    <rect x="679" y="803" width="12" height="8" fill="var(--heading)"/>
    <path d="M679 803 l6 4 6 -4" fill="none" stroke="var(--paper)" stroke-width="1"/>
    <text class="contact" x="691" y="842" font-size="19" fill="var(--ink)">www.amberhillhouse.example</text>
  </g>
</svg>
</body>
</html>
```